plovu business card design

plovu is an incubator within RTM Media focused on unlocking the potential in underserved niche micro-verticals on the web. our mission is to rapidly develop and foster emerging micro-verticals bc they are ripe for growth - building interesting and trusted content experiences with unqiue, useful and cutting-edge delivery methods.please do all copy (except for RTM Media, which must look as typed here and in logo) in all lowercase. Also please use spaces between phone # extensions not dashes or periods. I have attached all variations of the logo.
Industry/Entity Type
Business
Contact Information for Business Card
daria feltow, ceo www.plovu.io 218 holbrook lane 3rd floor oakland ca 94731 415 602 0002m 510 985 7966d daria.feltow@plovu.io
Look and feel
Each slider illustrates characteristics of the customer's brand and the style your logo design should communicate.

```html
<!DOCTYPE html>
<html lang="en">
<head>
<meta charset="utf-8">
<title>plovu business card</title>
<link rel="stylesheet" href="https://fonts.googleapis.com/css2?family=Source+Sans+3:wght@400;600&family=Quicksand:wght@500;600&display=swap">
<style>
  :root {
    --ink-black: #231f20;
    --teal: #00827f;
    --teal-deep: #006a68;
    --paper: #ffffff;
    --backdrop: #ecebe8;
    --text-dark: #2b2b2b;
  }
  * { margin: 0; padding: 0; box-sizing: border-box; }
  html, body {
    width: 1200px; height: 900px; overflow: hidden;
    background: var(--backdrop);
  }
  .canvas { position: relative; width: 1200px; height: 900px; }

  .card {
    position: absolute;
    box-shadow: 0 6px 18px rgba(0,0,0,0.18);
    overflow: hidden;
  }

  /* front */
  .card-front {
    left: 238px; top: 60px; width: 555px; height: 345px;
    background: var(--ink-black);
    font-family: "Source Sans 3", "Myriad Pro", sans-serif;
    color: var(--paper);
  }
  .card-front .sweep { position: absolute; inset: 0; }
  .card-front .splash-art {
    position: absolute; left: 14px; top: 100px; width: 200px; height: 200px;
  }
  .holder-name {
    position: absolute; left: 46px; top: 28px;
    font-size: 20px; font-weight: 600; line-height: 1;
  }
  .holder-role {
    position: absolute; left: 46px; top: 52px;
    font-size: 15px; font-weight: 400; line-height: 1;
  }
  .contact-list {
    position: absolute; right: 22px; top: 180px;
    list-style: none; text-align: right;
    font-size: 15px; line-height: 23px;
  }
  .contact-list li { display: flex; justify-content: flex-end; align-items: center; gap: 8px; }
  .contact-list .icon { width: 12px; height: 12px; flex: none; }
  .contact-address {
    position: absolute; right: 29px; top: 277px;
    text-align: right; font-size: 15px; line-height: 21px;
  }

  /* back */
  .card-back {
    left: 457px; top: 517px; width: 560px; height: 345px;
    background: var(--paper);
    text-align: center;
    font-family: "Quicksand", "Source Sans 3", sans-serif;
    color: var(--text-dark);
  }
  .brand-lockup {
    position: absolute; left: 0; right: 0; top: 96px;
    display: flex; justify-content: center; align-items: center; gap: 14px;
  }
  .brand-name {
    font-size: 88px; font-weight: 600; line-height: 1; letter-spacing: -1px;
    color: var(--ink-black);
  }
  .brand-dot {
    width: 26px; height: 26px; border-radius: 50%;
    background: var(--teal); margin-top: 18px;
  }
  .brand-tagline {
    position: absolute; left: 0; right: 0; top: 211px;
    font-size: 19px; font-weight: 500; letter-spacing: 0.3px;
  }
  .brand-url {
    position: absolute; left: 0; right: 0; top: 263px;
    font-size: 19px; font-weight: 500; letter-spacing: 3px;
  }
  .brand-url .accent { color: var(--teal); }
</style>
</head>
<body>
<main class="canvas">

  <section class="card card-front">
    <svg class="sweep" viewBox="0 0 555 345" width="555" height="345" aria-hidden="true">
      <path d="M555 0 C470 150 330 270 40 300 L0 302 L0 345 L555 345 Z" fill="var(--teal)"/>
    </svg>
    <div class="splash-art" role="img" aria-label="teal ink splash dripping into the black area"
         style="background: radial-gradient(ellipse at 40% 75%, rgba(0,130,127,0.55), rgba(0,130,127,0) 70%);"></div>

    <p class="holder-name">daria feltow</p>
    <p class="holder-role">ceo</p>

    <ul class="contact-list">
      <li>415 738 4196
        <svg class="icon" viewBox="0 0 12 12" aria-hidden="true"><path d="M2.5 0.8 L4.3 3.3 L3.4 4.5 C4 6 5.8 7.9 7.5 8.6 L8.7 7.7 L11.2 9.5 L10.2 11.2 C5.5 11 1 6.5 0.8 1.8 Z" fill="#fff"/></svg>
      </li>
      <li>510 247 3859
        <svg class="icon" viewBox="0 0 12 12" aria-hidden="true"><path d="M2.5 0.8 L4.3 3.3 L3.4 4.5 C4 6 5.8 7.9 7.5 8.6 L8.7 7.7 L11.2 9.5 L10.2 11.2 C5.5 11 1 6.5 0.8 1.8 Z" fill="#fff"/></svg>
      </li>
      <li>daria.feltow@plovu.io
        <svg class="icon" viewBox="0 0 12 12" aria-hidden="true"><rect x="0.5" y="2.5" width="11" height="7.5" fill="#fff"/><path d="M0.8 2.9 L6 7 L11.2 2.9" fill="none" stroke="var(--teal)" stroke-width="1"/></svg>
      </li>
      <li>www.plovu.io
        <svg class="icon" viewBox="0 0 12 12" aria-hidden="true"><g fill="none" stroke="#fff" stroke-width="1.4"><rect x="0.9" y="5.2" width="6" height="3.4" rx="1.7" transform="rotate(-45 3.9 6.9)"/><rect x="5.1" y="3.4" width="6" height="3.4" rx="1.7" transform="rotate(-45 8.1 5.1)"/></g></svg>
      </li>
    </ul>

    <address class="contact-address" style="font-style: normal;">
      218 holbrook lane 3rd<br>floor oakland ca 94731
    </address>
  </section>

  <section class="card card-back">
    <div class="brand-lockup">
      <span class="brand-name">plovu</span>
      <span class="brand-dot" aria-hidden="true"></span>
    </div>
    <p class="brand-tagline">an RTM Media publishing incubator</p>
    <p class="brand-url">www.<span class="accent">plovu</span>.io</p>
  </section>

</main>
</body>
</html>
```